"Rise. Shift. Thrive." Empowerment Book Cover

Hello, I need a hot, trendy, and contemporary book cover designed for my first book called "Rise. Shift. Thrive. -- 360 Bold Momentum Notes to Guide Anyone to Rise, Shift, and Thrive in Their Career & Daily Dreams."
This is my first book and I am really wanting to launch my brand with it... it would be awesome to match the inside/outside branding of the book. So we can either create the book cover to match the book guts, or update the book guts to match the cover.
Lastly, I just got a professional photoshoot done last week so we can use one of those images, or we can go with a different idea/style for the cover. The body of the book is attached. All questions welcomed, happy designing!
Target Market(s)
Gen Z, Millennials and Gen X.
Industry/Entity Type
Personal Development.
Requirements
Must have
- It must stand out and be different from other typical book covers.
Nice to have
- Success, Inspiration, Motivation, Mindset, Growth.
Should not have
- Clipart, stock art, stock look and feel.

```html
<!DOCTYPE html>
<html lang="en">
<head>
<meta charset="utf-8">
<title>Rise. Shift. Thrive. — Book Cover</title>
<link href="https://fonts.googleapis.com/css2?family=Jost:wght@400;700&display=swap" rel="stylesheet">
<style>
  :root {
    --cover-bg: #b3b3b3;
    --title-light: #ffffff;
    --title-mid: #666666;
    --title-dark: #000000;
    --subtitle-ink: #111111;
    --author-ink: #ffffff;
  }
  * { margin: 0; padding: 0; box-sizing: border-box; }
  html, body {
    width: 752px;
    height: 1200px;
    overflow: hidden;
    background: var(--cover-bg);
  }
  .cover {
    position: relative;
    width: 752px;
    height: 1200px;
    background: var(--cover-bg);
    font-family: "Jost", "Futura", sans-serif;
  }
  .title {
    position: absolute;
    left: 96px;
    top: 0;
    font-weight: 400;
    font-size: 162px;
    letter-spacing: -1px;
  }
  .title-line {
    position: absolute;
    left: 0;
    white-space: nowrap;
    line-height: 1;
  }
  .title-line--first  { top: 6px;   color: var(--title-light); }
  .title-line--second { top: 178px; color: var(--title-mid); }
  .title-line--third  { top: 348px; color: var(--title-dark); }

  .subtitle {
    position: absolute;
    left: 230px;
    top: 620px;
    width: 500px;
    color: var(--subtitle-ink);
    font-weight: 400;
    font-size: 20.5px;
    line-height: 37px;
  }
  .subtitle span { display: block; white-space: nowrap; }

  .author {
    position: absolute;
    left: 90px;
    top: 600px;
    width: 70px;
    height: 568px;
  }
  .author text {
    font-family: "Jost", "Futura", sans-serif;
    font-weight: 700;
    font-size: 82px;
    fill: var(--author-ink);
  }
</style>
</head>
<body>
  <main class="cover">
    <h1 class="title">
      <span class="title-line title-line--first">Rise.</span>
      <span class="title-line title-line--second">Shift.</span>
      <span class="title-line title-line--third">Thrive.</span>
    </h1>

    <p class="subtitle">
      <span>360 Bold Momentum NOTES</span>
      <span>to Guide Anyone to RISE, SHIFT, and THRIVE</span>
      <span>in Their Career &amp; Daily Dreams.</span>
    </p>

    <svg class="author" viewBox="0 0 70 568" aria-label="Samir Haddad">
      <text transform="translate(64 566) rotate(-90)" textLength="560" lengthAdjust="spacing">Samir Haddad</text>
    </svg>
  </main>
</body>
</html>
```